Diaper Crisis Infographic

We are a homeless shelter. Among other things we provide diapers, formula, and other basic necessities for homeless families. We give out over 5,500 diapers each month! We are holding a diaper drive in the month of August to help bolster our supply of diapers. This infographic will be to share via social media to help people to see the incredible need and inspire them to donate diapers or hold diaper drives themselves.

It just so happens that the Review of Childhood Medicine just released a study that has some pertinent information regarding the "Diaper Crisis" among low income families in America.

Here is the key data from the study:

1 in 3 mothers cut back on essentials (food, child care, utilities) to afford diapers
A single mother working full time at min wage would use 6% of gross income on diapers, that's $18 a week for diapers on avg ($936 a year)
8%(1 in 12) of women interviewed had stretched a diaper by leaving a wet one on longer or partially cleaning and reusing it.
30% of mothers had experienced a time when they could not afford to buy the diapers their kids needed.
10% turned to family or friends
10% turned to an agency or diaper bank
3% turned to other sources like a church
Worry about how to pay for diapers in among top stressors for low income parents, next to food and housing.
Our Pelwick Home program gives out 5500 diapers a month

A summary article of the study can be found here http://www.trevonwire.example/health/it-made-me-feel-ashamed-poor-moms-anguish-over-diaper-6C10775589 and here http://www.dorvalgazette.example/news/science/dg-sci-diaper-need-20130729,0,1515372.story

You can see our color scheme at http://brindlehaven.example/ Not looking for an exact match on the colors or design, but something that flows well would be nice. http://www.brindlehaven.example/diapers has the video that goes along with the diaper drive.

Target Market(s)

Individuals, age 30+

Industry/Entity Type

Church

Requirements
Must have
• Images of babies and or diapers as the graphics. Must include the Lantern & Hearth logo but doesn't need to be prominently displayed. Logo can be green, black, or white.

```html
<!DOCTYPE html>
<html lang="en">
<head>
<meta charset="utf-8">
<title>Diaper Crisis Infographic</title>
<link href="https://fonts.googleapis.com/css2?family=Oswald:wght@400;600;700&family=Open+Sans:wght@400;600;700&display=swap" rel="stylesheet">
<style>
  :root {
    --green-deep: #2c7a30;
    --green: #3f9b3c;
    --green-light: #5cb24a;
    --lime: #c5d92d;
    --charcoal: #4a4f4a;
    --white: #ffffff;
    --ink: #1f2a1f;
    --blue: #2aa6e0;
    --grey: #bdbdbd;
    --orange: #f5821f;
    --red: #d7262b;
  }
  * { margin: 0; padding: 0; box-sizing: border-box; }
  html, body { width: 1200px; height: 2572px; overflow: hidden; }
  body {
    position: relative;
    font-family: "Open Sans", sans-serif;
    color: var(--white);
    background: radial-gradient(ellipse at 50% 35%, var(--green-light) 0%, var(--green) 45%, var(--green-deep) 100%);
  }
  .hero-art {
    position: absolute; left: 240px; top: 30px; width: 720px; height: 470px;
    border-radius: 24px;
    background: linear-gradient(180deg, rgba(255,255,255,0.28), rgba(255,255,255,0.12));
  }
  .headline-block { position: absolute; left: 0; top: 540px; width: 1200px; height: 360px; }
  .headline-block .lime-square {
    position: absolute; left: 470px; top: 0; width: 260px; height: 340px; background: var(--lime);
  }
  .headline-block .dark-band {
    position: absolute; left: 380px; top: 110px; width: 440px; height: 250px;
    background: var(--charcoal); text-align: center; padding-top: 6px;
  }
  .ratio { font-family: "Oswald", sans-serif; font-weight: 700; font-size: 120px; line-height: 1; }
  .ratio-subject { font-family: "Oswald", sans-serif; font-weight: 700; font-size: 64px; color: var(--lime); line-height: 1; margin-top: 4px; }
  .ratio-note { font-size: 26px; line-height: 1.25; margin-top: 8px; }

  .wage-strip { position: absolute; left: 0; top: 1010px; width: 1200px; height: 200px; }
  .wage-strip .mother-icon {
    position: absolute; left: 40px; top: 30px; width: 110px; height: 150px;
    border-radius: 12px; background: rgba(255,255,255,0.85);
  }
  .wage-strip .lime-bar {
    position: absolute; left: 170px; top: 10px; width: 1030px; height: 180px;
    background: var(--lime); text-align: center; color: var(--ink); padding-top: 16px;
  }
  .wage-lead { font-size: 26px; }
  .wage-share { font-size: 30px; margin-top: 6px; }
  .wage-share strong, .wage-amount strong { font-family: "Oswald", sans-serif; font-size: 44px; }
  .wage-amount { font-family: "Oswald", sans-serif; font-size: 36px; margin-top: 2px; }
  .wage-share strong, .wage-amount { color: var(--white); }

  .stat-row { position: absolute; left: 32px; top: 1260px; width: 1148px; display: flex; gap: 12px; align-items: flex-start; }
  .stat { width: 220px; }
  .stat-figure { font-family: "Oswald", sans-serif; font-weight: 600; font-size: 72px; text-align: center; height: 120px; line-height: 120px; }
  .stat-text { padding: 14px 16px; font-size: 22px; line-height: 1.3; color: var(--ink); background: rgba(255,255,255,0.82); }
  .stat.blue .stat-figure { background: var(--blue); }
  .stat.blue .stat-text { background: #8fd0ef; color: var(--white); height: 300px; }
  .stat.grey .stat-figure { background: var(--grey); }
  .stat.grey .stat-text { background: #e4e4e4; height: 300px; }
  .stat.orange .stat-figure { background: var(--orange); }
  .stat.orange .stat-text { background: #fbc08c; height: 130px; }
  .stat.lime .stat-figure { background: var(--lime); }
  .stat.lime .stat-text { background: #e3ec9a; height: 150px; }
  .stat.red .stat-figure { background: var(--red); }
  .stat.red .stat-text { background: #ec9496; height: 150px; }

  .stress-band {
    position: absolute; left: 0; top: 1830px; width: 1200px; height: 150px;
    background: rgba(20,60,22,0.35); text-align: center; font-size: 40px; line-height: 1.3; padding-top: 18px;
  }
  .program { position: absolute; left: 0; top: 2020px; width: 1200px; text-align: center; }
  .program-lead { font-family: "Oswald", sans-serif; font-weight: 600; font-size: 52px; color: var(--lime); }
  .program-count { font-family: "Oswald", sans-serif; font-weight: 700; font-size: 80px; line-height: 1.1; }

  .brand { position: absolute; left: 0; top: 2300px; width: 1200px; display: flex; flex-direction: column; align-items: center; gap: 14px; }
  .brand-mark { width: 90px; height: 90px; border-radius: 50%; background: var(--white); }
  .brand-name { font-family: "Oswald", sans-serif; font-weight: 600; font-size: 56px; color: var(--white); }
</style>
</head>
<body>
  <div class="hero-art" role="img" aria-label="Balance scale weighing a diaper against a globe of everyday food essentials held in two hands"></div>

  <section class="headline-block">
    <div class="lime-square"></div>
    <div class="dark-band">
      <div class="ratio">1 in 3</div>
      <div class="ratio-subject">mothers</div>
      <div class="ratio-note">cut back on essentials<br>to afford diapers</div>
    </div>
  </section>

  <section class="wage-strip">
    <div class="mother-icon" role="img" aria-label="Icon of a mother holding a baby"></div>
    <div class="lime-bar">
      <p class="wage-lead">A single mother working full time at min wage would use</p>
      <p class="wage-share"><strong>6%</strong> of gross income on diapers,</p>
      <p class="wage-amount">that's <strong>$18 a week</strong> for diapers on avg <strong>($936 a year)</strong></p>
    </div>
  </section>

  <section class="stat-row">
    <div class="stat blue">
      <div class="stat-figure">8%</div>
      <p class="stat-text">(1 in 12) of women interviewed had stretched a diaper by leaving a wet one on longer or partially cleaning and reusing it.</p>
    </div>
    <div class="stat grey">
      <div class="stat-figure">30%</div>
      <p class="stat-text">of mothers had experienced a time when they could not afford to buy the diapers their kids needed.</p>
    </div>
    <div class="stat orange">
      <div class="stat-figure">10%</div>
      <p class="stat-text">turned to family or friends</p>
    </div>
    <div class="stat lime">
      <div class="stat-figure">10%</div>
      <p class="stat-text">turned to an agency or diaper bank</p>
    </div>
    <div class="stat red">
      <div class="stat-figure">3%</div>
      <p class="stat-text">turned to other sources like a church</p>
    </div>
  </section>

  <p class="stress-band">Worry about how to pay for diapers<br>in among top stressors for low income parents, next to food and housing.</p>

  <section class="program">
    <p class="program-lead">Our Pelwick Home program gives out</p>
    <p class="program-count">5500 diapers a month</p>
  </section>

  <footer class="brand">
    <div class="brand-mark"></div>
    <div class="brand-name">Lantern &amp; Hearth</div>
  </footer>
</body>
</html>
```